Website design for commercial and residential security company

we're looking to see some new designs for an established company with no website.

homepage and one inner page

here is a link to the homepage content, sitemap, logo and more.
https://files.brontavel.net/share/7QxmPzLrTw2vNkdJhYcsa9eFgbUoiVwRn?view=open

call to action should be Request A Quote

if you have any questions please send them to us asap

thank you

1 page

Sans Serif

```html
<!DOCTYPE html>
<html lang="en">
<head>
<meta charset="utf-8">
<title>Beacon Ridge Security Group</title>
<link rel="stylesheet" href="https://fonts.googleapis.com/css2?family=Archivo:wght@800&family=Poppins:wght@300;400;500&family=Roboto:wght@400;500;700&display=swap">
<style>
:root{
  --gold:#d4a135;
  --gold-deep:#c08c22;
  --gold-soft:#e2b85a;
  --ink:#111111;
  --text:#1e1e1e;
  --muted:#666666;
  --grey:#5c5c5c;
  --white:#ffffff;
}
*{box-sizing:border-box;margin:0;padding:0}
html,body{width:1200px;height:3919px;overflow:hidden;background:var(--white)}
body{position:relative;font-family:"Poppins",sans-serif;color:var(--text)}
.abs{position:absolute}
.btn-dark{position:absolute;background:var(--ink);color:var(--white);font:500 14px "Roboto",sans-serif;display:flex;align-items:center;justify-content:center;border-radius:3px;letter-spacing:.3px}
.brand{display:flex;align-items:center;gap:10px;font:500 30px "Roboto",sans-serif;color:#8a8a8a;letter-spacing:1px}
.brand-dot{width:18px;height:18px;border-radius:50%;background:var(--gold)}

/* hero */
.hero{position:absolute;left:0;top:0;width:1200px;height:745px;overflow:hidden}
.hero-photo{position:absolute;inset:0;background:linear-gradient(100deg,#e9e7e3 0%,#dcd6cc 40%,#d9b879 70%,#c8902d 100%)}
.hero-title{position:absolute;right:64px;top:252px;text-align:right;font:800 44px/56px "Archivo",sans-serif;color:var(--ink);letter-spacing:-.5px}
.hero-edge{position:absolute;left:0;top:625px}

/* mission */
.mission-title{left:152px;top:888px;font:500 22px "Roboto",sans-serif;color:var(--ink)}
.mission-lead{left:152px;top:944px;width:390px;font:400 14.5px/23px "Roboto",sans-serif}
.mission-body{left:152px;top:1036px;width:390px;font:300 12px/20px "Poppins",sans-serif;color:var(--muted)}
.photo-side{left:695px;top:890px;width:70px;height:235px;background:linear-gradient(180deg,#d8d8d8,#8f8f8f);border:5px solid var(--white);box-shadow:0 4px 14px rgba(0,0,0,.15)}
.photo-main{left:762px;top:828px;width:378px;height:338px;border:8px solid var(--white);box-shadow:0 4px 18px rgba(0,0,0,.18);background:linear-gradient(135deg,#f2f2f0,#d5dbe2 60%,#8aa2bf)}

/* gold bands */
.band{position:absolute;left:0;width:1200px;background:linear-gradient(90deg,var(--gold) 0%,var(--gold-soft) 55%,var(--gold) 100%)}
.commercial{top:1247px;height:685px;clip-path:polygon(0 93px,50% 0,100% 93px,100% 593px,50% 685px,0 593px)}
.commercial-photo{left:108px;top:136px;width:376px;height:375px;background:linear-gradient(160deg,#d9d2c6,#a69a86 55%,#2a2a2a)}
.commercial-copy{left:552px;top:138px;width:480px;color:var(--white)}
.commercial-copy h2{font:500 22px "Roboto",sans-serif;margin-bottom:14px}
.commercial-copy .lead{font:400 13px/21px "Poppins",sans-serif;margin-bottom:12px}
.commercial-copy .body{font:300 11.5px/20px "Poppins",sans-serif;margin-bottom:8px}
.checks{list-style:none}
.checks li{display:flex;gap:12px;font:300 11.5px/20px "Poppins",sans-serif;margin-bottom:13px}
.checks svg{flex:none;margin-top:2px}

/* approach */
.approach{left:61px;top:2040px;width:460px}
.approach .lead{font:400 14.5px/23px "Roboto",sans-serif;color:var(--ink);margin-bottom:14px}
.approach p{font:300 11.5px/20px "Poppins",sans-serif;color:var(--muted);margin-bottom:10px}
.cameras-photo{left:555px;top:2030px;width:645px;height:355px;background:radial-gradient(ellipse at 50% 45%,#f5f5f5 0%,#e3e3e3 55%,#ffffff 80%)}

/* quote */
.quote{top:2494px;height:601px;clip-path:polygon(0 91px,50% 0,100% 91px,100% 511px,50% 601px,0 511px)}
.quote h2{position:absolute;font:500 22px "Roboto",sans-serif;color:var(--white)}
.info{position:absolute;left:187px;display:flex;gap:35px;color:var(--white)}
.info .icon{width:46px;height:46px;border-radius:50%;background:var(--ink);display:flex;align-items:center;justify-content:center;flex:none}
.info b{display:block;font:400 16px "Roboto",sans-serif;margin-top:0}
.info span{font:300 11.5px/20px "Poppins",sans-serif}
.field{position:absolute;left:596px;width:360px;height:36px;background:rgba(255,255,255,.22);border-radius:3px;color:var(--white);font:300 11.5px "Poppins",sans-serif;padding:8px 9px}
.submit{position:absolute;left:596px;top:476px;width:127px;height:36px;background:var(--white);color:var(--ink);font:700 13px "Roboto",sans-serif;display:flex;align-items:center;justify-content:center;border-radius:3px}

/* residential */
.phone-photo{left:90px;top:3133px;width:410px;height:510px;z-index:2;background:linear-gradient(180deg,#2b2b2b 0%,#6a7b6a 60%,#c89474 100%);border-radius:40px 40px 20px 20px}
.residential{left:657px;top:3185px;width:400px}
.residential h2{font:500 22px "Roboto",sans-serif;color:var(--ink);margin-bottom:18px}
.residential .lead{font:400 14px/22px "Roboto",sans-serif;margin-bottom:12px}
.residential p{font:300 11.5px/22px "Poppins",sans-serif;color:var(--muted)}

/* footer */
.footer{top:3555px;height:364px;clip-path:polygon(0 85px,50% 0,100% 85px,100% 100%,0 100%)}
.footer .brand{position:absolute;left:0;width:1200px;top:92px;justify-content:center;color:var(--white);font-size:28px}
.footer .brand-dot{background:var(--white)}
.nav{position:absolute;left:0;width:1200px;top:180px;display:flex;justify-content:center;gap:22px;color:var(--white);font:400 12px "Poppins",sans-serif}
.rule{position:absolute;left:300px;width:600px;top:226px;height:1px;background:rgba(255,255,255,.35)}
.social{position:absolute;left:0;width:1200px;top:247px;display:flex;justify-content:center;gap:12px}
.social i{width:32px;height:32px;border-radius:50%;background:var(--white);display:block}
.copy{position:absolute;left:0;width:1200px;top:330px;text-align:center;color:var(--white);font:300 11px "Poppins",sans-serif}
</style>
</head>
<body>

<section class="hero">
  <div class="hero-photo" role="img" aria-label="Hand pressing the keypad of a wall-mounted alarm panel"></div>
  <div class="abs brand" style="left:62px;top:32px"><span class="brand-dot"></span>BEACON RIDGE</div>
  <a class="btn-dark" style="left:987px;top:43px;width:153px;height:37px">REQUEST A QUOTE</a>
  <h1 class="hero-title">PROTECT ASSETS AND<br>SECURITY OF YOUR<br>BUSINESS</h1>
  <a class="btn-dark" style="left:1001px;top:447px;width:139px;height:37px">CONTACT US</a>
  <svg class="hero-edge" width="1200" height="120" viewBox="0 0 1200 120">
    <polygon points="0,55 600,110 1200,15 1200,120 0,120" fill="#ffffff"/>
    <polygon points="0,30 470,110 0,75" fill="#d4a135"/>
    <polygon points="1200,35 730,110 1200,75" fill="#d4a135"/>
    <polygon points="0,100 330,120 0,120" fill="#5c5c5c"/>
    <polygon points="1200,100 880,120 1200,120" fill="#5c5c5c"/>
  </svg>
</section>

<h2 class="abs mission-title">Our Mission</h2>
<p class="abs mission-lead">To provide our customers with comprehensive security, audio/video, and automation with top notch customer service. We Ensure Security with Smart Tools.</p>
<p class="abs mission-body">The graded security measures from Beacon Ridge Security Group ensure the safety of both residential and commercial property. We provide a wide range of Residential and Commercial Security Solutions.</p>
<div class="abs photo-side" role="img" aria-label="Video doorbell mounted on a door frame"></div>
<div class="abs photo-main" role="img" aria-label="Woman using a wall-mounted smart home control panel"></div>

<section class="band commercial">
  <div class="abs commercial-photo" role="img" aria-label="Security touch panel on a table in a bright hallway"></div>
  <div class="abs commercial-copy">
    <h2>Commercial Solutions</h2>
    <p class="lead">Protect assets and security of your business with Exceptional Commercial Security Installation</p>
    <p class="body">People's safety is our top priority. This includes ensuring that the security system built at your commercial property is configured accurately. Further, it will protect against intruders, burglaries, and holdups. We do this by:</p>
    <ul class="checks">
      <li><svg width="18" height="18" viewBox="0 0 18 18"><circle cx="9" cy="9" r="7.5" fill="none" stroke="#fff" stroke-width="1.4"/><path d="M5.5 9.2l2.4 2.4 5-5" fill="none" stroke="#fff" stroke-width="1.6"/></svg>Audio &amp; Video Solutions for your commercial property</li>
      <li><svg width="18" height="18" viewBox="0 0 18 18"><circle cx="9" cy="9" r="7.5" fill="none" stroke="#fff" stroke-width="1.4"/><path d="M5.5 9.2l2.4 2.4 5-5" fill="none" stroke="#fff" stroke-width="1.6"/></svg>Burglar Alarms &amp; Detectors</li>
      <li><svg width="18" height="18" viewBox="0 0 18 18"><circle cx="9" cy="9" r="7.5" fill="none" stroke="#fff" stroke-width="1.4"/><path d="M5.5 9.2l2.4 2.4 5-5" fill="none" stroke="#fff" stroke-width="1.6"/></svg>CCTV cameras equipped with facial recognition technologies enable the technology to identify the offenders.</li>
      <li><svg width="18" height="18" viewBox="0 0 18 18"><circle cx="9" cy="9" r="7.5" fill="none" stroke="#fff" stroke-width="1.4"/><path d="M5.5 9.2l2.4 2.4 5-5" fill="none" stroke="#fff" stroke-width="1.6"/></svg>Monitoring of alarms and video recordings 24 hours a day, seven days a week. Addressing all the incidents with an urgent response.</li>
      <li><svg width="18" height="18" viewBox="0 0 18 18"><circle cx="9" cy="9" r="7.5" fill="none" stroke="#fff" stroke-width="1.4"/><path d="M5.5 9.2l2.4 2.4 5-5" fill="none" stroke="#fff" stroke-width="1.6"/></svg>Alarm systems and cameras precisely installed so that more of your property is tracked.</li>
    </ul>
  </div>
</section>

<div class="abs approach">
  <p class="lead">We will help secure your company outside of the realm of conventional monitoring technologies. Indeed, we take a customised and comprehensive approach to defence.</p>
  <p>Flooding, smoke, power outages, temperature fluctuations, and other factors will all be tracked. So, you can take prompt steps before you experience damage.</p>
  <p>But, it all comes down to internal and external security measures.</p>
  <p>We can combine low-light cameras, smoke and temperature monitoring, noise control, and physical surveillance into a 24/7 commercial security solution. Thus, you can focus on running your business with utmost safety.</p>
  <p>Our commercial security services are comprehensive. In fact, we have worked out how to protect companies from future threats by tailoring our strategy to each new customer. Therefore, whatever business you are into, we provide you with a security solution that physically protects you, your employees, clients, and property.</p>
</div>
<div class="abs cameras-photo" role="img" aria-label="Row of four white wireless security cameras"></div>

<section class="band quote">
  <h2 style="left:189px;top:174px">Get A Quote</h2>
  <div class="info" style="top:221px">
    <div class="icon"><svg width="20" height="20" viewBox="0 0 20 20"><path d="M10 2a5.5 5.5 0 0 0-5.5 5.5C4.5 12 10 18 10 18s5.5-6 5.5-10.5A5.5 5.5 0 0 0 10 2z" fill="none" stroke="#fff" stroke-width="1.5"/><circle cx="10" cy="7.5" r="2" fill="#fff"/></svg></div>
    <div><b>Address</b><span>Lorem Ipsum is simply dummy<br>text of the printing.</span></div>
  </div>
  <div class="info" style="top:318px">
    <div class="icon"><svg width="20" height="20" viewBox="0 0 20 20"><path d="M5 2.5l3 3-1.6 2.2a10 10 0 0 0 5.9 5.9L14.5 12l3 3-2 2.5C9 17 3 11 2.5 4.5z" fill="#fff"/></svg></div>
    <div><b>Call</b><span>Count details</span></div>
  </div>
  <div class="info" style="top:425px">
    <div class="icon"><svg width="20" height="16" viewBox="0 0 20 16"><rect x="1" y="1" width="18" height="14" rx="1.5" fill="#fff"/><path d="M1.5 2l8.5 7 8.5-7" fill="none" stroke="#111" stroke-width="1.4"/></svg></div>
    <div><b>Mail</b><span>Installation....</span></div>
  </div>
  <h2 style="left:594px;top:174px">Contact Us</h2>
  <div class="field" style="top:221px">Name:</div>
  <div class="field" style="top:266px">Email:</div>
  <div class="field" style="top:311px">Phone:</div>
  <div class="field" style="top:356px;height:105px">Message:</div>
  <div class="submit">SUBMIT</div>
</section>

<div class="abs phone-photo" role="img" aria-label="Hand holding a smartphone showing a home security app with camera views"></div>
<div class="abs residential">
  <h2>Residential Security Solutions</h2>
  <p class="lead">Consider a home surveillance device that would do more for you and your family than you ever imagined.</p>
  <p>Beacon Ridge Security Group is your trustable security provider. Also, as certified professionals carry out the installation, you have everything under control. Your home is being securely watched from various points, with cameras capable of tracking any intruder's path. Specifically, we offer Residential Intrusion Detection Security Systems, Residential Alarm, Residential Network Wi-Fi, CCTVs and residential home automation.</p>
</div>

<footer class="band footer">
  <div class="brand"><span class="brand-dot"></span>BEACON RIDGE</div>
  <nav class="nav"><span>Home</span><span>|</span><span>About Us</span><span>|</span><span>Solution</span><span>|</span><span>Resources</span><span>|</span><span>Contact Us</span></nav>
  <div class="rule"></div>
  <div class="social"><i></i><i></i><i></i></div>
  <p class="copy">2021 ©BEACON RIDGE - All Right Reserved.</p>
</footer>

</body>
</html>
```